Cool blackchain based app company needs a website :)

pillcheckhub.net

Kinda says it all!! This is an app which sits on your smartfone / tablet. You scan a QR code from a medicinal product and our app will verify if the product you have is genuine. It's simple, It's free.

The design could be very modern and simple. It should show in graphical form how the app works and have FAQ's etc.

pillcheckhub.net is designed specifically to allow consumers verify that the medical products which they have purchased are genuine.

Detailed brief with content attached. Logo in high res and QR code attached.

Full website required.
Updates

Target Market(s)

Pharmaceutical

Industry/Entity Type

Pharmaceutical

Coding

Coded - Design and coding required

Number of Pages Required

3 page

Colors

Designer to choose colors to be used in the design.

Requirements
Must have
• Strong visuals - very simple navigation - 3 pages
Nice to have
• Animation of the process
Should not have
• Jargon!

```html
<!DOCTYPE html>
<html lang="en">
<head>
<meta charset="utf-8">
<title>pillcheckhub.net</title>
<link rel="stylesheet" href="https://fonts.googleapis.com/css2?family=Open+Sans:wght@400;700&family=Playfair+Display:wght@700&display=swap">
<style>
:root{
  --page:#ffffff;
  --brand-blue:#1e73be;
  --brand-green:#3a9a3c;
  --logo-text:#1e4f8c;
  --panel:#2e2e2e;
  --panel-line:#3a3a3a;
  --panel-text:#e6b768;
  --panel-head:#f4f4f4;
  --icon-ring:#d8d8d8;
  --stage:#141414;
}
*{margin:0;padding:0;box-sizing:border-box}
html,body{width:864px;height:1200px;overflow:hidden;background:var(--page)}
body{position:relative;font-family:"Open Sans",Arial,sans-serif}

.site-header{position:absolute;left:87px;top:0;width:690px;height:67px;
  background:linear-gradient(#f4f4f4,#ffffff)}
.brand{position:absolute;left:56px;top:6px;width:110px;text-align:center}
.brand-dot{display:block;width:38px;height:38px;margin:0 auto 4px;border-radius:50%;background:var(--brand-green)}
.brand-name{font-size:10px;font-weight:700;color:var(--logo-text);line-height:1}

.main-nav{position:absolute;left:374px;top:28px;display:flex;gap:11px}
.main-nav a{font-size:6.5px;font-weight:700;color:var(--brand-blue);text-decoration:none;letter-spacing:.1px}
.social{position:absolute;left:576px;top:26px;display:flex;gap:3px}
.social span{width:15px;height:15px;border-radius:50%;border:1px solid var(--icon-ring);background:#fff}

.hero{position:absolute;left:87px;top:77px;width:690px;height:407px;
  background:linear-gradient(90deg,#161616 0%,#1d1d1d 60%,#3a2a24 85%,#5a4036 100%)}
.player{position:absolute;left:81px;top:9px;width:518px;height:381px;background:#000}
.player-title{position:absolute;left:9px;top:8px;font-size:8.5px;color:#fff}
.player-tools{position:absolute;right:10px;top:7px}
.player-slide{position:absolute;left:0;top:48px;width:518px;height:284px;
  background:linear-gradient(135deg,#ffffff 0%,#f2f6fa 60%,#e9e3dc 100%)}
.play-btn{position:absolute;left:243px;top:176px}

.section-title{position:absolute;left:0;top:552px;width:864px;text-align:center;
  font-family:"Playfair Display",Georgia,serif;font-weight:700;font-size:17px;color:var(--brand-blue);letter-spacing:-.2px}

.guarantees{position:absolute;left:174px;top:591px;width:508px;height:580px;background:var(--panel);border:1px solid #1a1a1a}
.guarantees .band{position:absolute;left:0;top:213px;width:100%;height:1px;background:var(--panel-line)}
.guarantee{position:absolute;left:10px;width:488px;color:var(--panel-text);font-size:10.6px;line-height:9.1px}
.guarantee h3{font-family:"Playfair Display",Georgia,serif;font-weight:700;font-size:12px;line-height:14px;
  color:var(--panel-head);text-align:center;margin-bottom:21px}
.guarantee p{margin-bottom:7px}
.guarantee ul{list-style:none;padding-left:14px}
.guarantee li{position:relative}
.guarantee li::before{content:"";position:absolute;left:-7px;top:3.5px;width:3px;height:3px;border-radius:50%;background:#888}
.g-auth{top:9px}.g-anon{top:129px}.g-sec{top:219px}.g-safe{top:390px}
</style>
</head>
<body>
<header class="site-header">
  <div class="brand"><span class="brand-dot"></span><span class="brand-name">pillcheckhub.net</span></div>
  <nav class="main-nav">
    <a href="#">HOME</a><a href="#">ABOUT US</a><a href="#">FAQS</a><a href="#">HOW TO USE</a><a href="#">CONTACT</a>
  </nav>
  <div class="social"><span></span><span></span><span></span></div>
</header>

<section class="hero">
  <div class="player">
    <div class="player-title">pch</div>
    <svg class="player-tools" width="30" height="12" viewBox="0 0 30 12">
      <circle cx="5" cy="6" r="5" fill="#fff"/><path d="M5 3v3h2.5" stroke="#000" stroke-width="1.2" fill="none"/>
      <path d="M18 10c1-4 4-6 8-6V1l4 4.5-4 4.5V7c-3 0-6 1-8 3z" fill="#fff"/>
    </svg>
    <div class="player-slide" role="img" aria-label="Explainer video still: a cartoon woman with a magnifying glass beside hand-written text asking if your medication is genuine"></div>
    <svg class="play-btn" width="34" height="24" viewBox="0 0 34 24">
      <rect width="34" height="24" rx="6" fill="#222" opacity=".9"/><path d="M13 7l10 5-10 5z" fill="#fff"/>
    </svg>
  </div>
</section>

<h2 class="section-title">Our Guarantees</h2>

<section class="guarantees">
  <span class="band"></span>
  <div class="guarantee g-auth">
    <h3>Guaranteed Authenticity</h3>
    <p>pillcheckhub has a unique and highly secure Blockchain database which contains details of billions of batches of medicines manufactured across the world</p>
    <p>Each time a manufacturer produces a batch of medicine, they send the details of that product to our secure Blockchain database.&nbsp; Our database records details of that batch of medicine and issues a unique encrypted QR code for every single batch.&nbsp; This code is printed on the medicine packet and it's packaging</p>
  </div>
  <div class="guarantee g-anon">
    <h3>Guaranteed Anonymity</h3>
    <ul>
      <li>Your health and personal information are yours, and only yours!</li>
      <li>pillcheckhub does NOT record any personal or health information</li>
      <li>You don't have to log on to pillcheckhub and we don't ask you to register</li>
    </ul>
  </div>
  <div class="guarantee g-sec">
    <h3>Guaranteed Security</h3>
    <p>pillcheckhub are the first and only company in the world to use a (patent pending) encrypted specifically designed secure Blockchain database architecture for asset recording and authentication</p>
    <p>A Blockchain database is made up of a large network of independent database servers, each of which are in sync with each other.&nbsp; As soon as a record is appended to the database, all instances of the database simultaneously update</p>
    <p>Every record added to the database must contain encrypted keys before it is accepted by the Blockchain database.&nbsp; These keys form an interlinking chain</p>
    <p>This multitude of in-sync databases and verified-chain data structure makes the pillcheckhub database impossible to hack</p>
  </div>
  <div class="guarantee g-safe">
    <h3>Guaranteed Safety</h3>
    <p>If you are taking medication you are doing so for a specific reason.&nbsp; It is imperative that your medication has been produced in accordance with strict international standards and that your medication contains the correct medicinal dosage</p>
    <p>The international pharmaceutical industry carefully manages their production processes to ensure the highest standards of product manufacture, production and distribution</p>
    <p>However, as in many industries, counterfeiting is a high value business.&nbsp; Counterfeit medicines cost the pharmaceutical industry more than €110 billion annually, €110 billion which otherwise would be invested into medical research and treatment development</p>
    <p>The financial cost is nothing compared to the loss of life.&nbsp; More than <em>one million people's lives</em> are lost each year due to counterfeit drugs.&nbsp; Counterfeit medicine often contains no active medicinal content or can contain a dangerous mix of ingredients.&nbsp; Whatever the mix, the medicine is not what it is claimed to be and the consequences of taking it can be lethal</p>
  </div>
</section>
</body>
</html>
```